Landing Page for our Applicants Page

Landing Page for the applicants for our QV campaign and as our company NOBLE POSTS ABROAD.WE OFFER JOBS IN ROYAL PALACES SO THE LANDING PAGE SHOULD REFLECT THAT. We have prepared the landing page leading page photo, logo and a landing page structure. We prefer a very classy and elegant page with not much colors - black and white and gray tones is nice with a nice photos. The main photo we have suggested and we will purchase if in case the designer will like it and we agree on the style. Here is the link to it https://www.pixmarketvault.example/ae/photo/beautiful-roses-and-baroque-rococo-style-palace-in-background-gm502938174-3197205 . WE ARE OPEN TO ANY PALACE PHOTO TO ATTRACT APPLICANTS TO US

Target Market(s)

Job Applicants, cleaners, nannies, cooks, nurses, tutors

Industry/Entity Type

Recruitment

Font styles to use
Serif

Requirements
Must have
• The sections that we have suggested. Our current web site if www.prime-homecrew.example you can use the partners logos from here and clients testimonials.
Nice to have
• If you have any other landing main photo that will suit more please suggest. This is only our recommendation and we have limited designers skills :). please we like clean designs - black and white lines and gray tones. Nothing too colorful. Classy and Clean.
Should not have
• We like one color palette, not numerous colors and mixed all together.

```html
<!DOCTYPE html>
<html lang="en">
<head>
<meta charset="utf-8">
<title>Noble Posts Abroad – Applicants</title>
<link rel="stylesheet" href="https://fonts.googleapis.com/css2?family=Lato:wght@400;700&display=swap">
<style>
:root{
  --ink:#1a1a1a;
  --dark:#141414;
  --darker:#0f0f0f;
  --paper:#ffffff;
  --mist:#f0f0f0;
  --line:#d8d8d8;
  --text:#333333;
  --badge:#3a3a3a;
}
*{box-sizing:border-box;margin:0;padding:0}
html,body{width:1200px;height:3928px;overflow:hidden}
body{font-family:'Lato',sans-serif;color:var(--text);background:var(--paper);position:relative}
.abs{position:absolute}
.section-title{position:absolute;left:0;width:1200px;text-align:center;font-size:33px;font-weight:400;letter-spacing:1px;text-transform:uppercase}

.site-header{position:absolute;top:0;left:0;width:1200px;height:98px;background:var(--paper)}
.brand{position:absolute;left:75px;top:52px;display:flex;align-items:center;gap:10px;font-size:19px;letter-spacing:1px;color:var(--ink)}
.brand-mark{width:14px;height:14px;border-radius:50%;background:var(--ink)}
.call{position:absolute;right:72px;top:38px;font-size:18px;font-weight:700;color:var(--ink);display:flex;align-items:center;gap:12px}
.main-nav{position:absolute;top:98px;left:0;width:1200px;height:52px;background:var(--ink);display:flex;padding-left:60px}
.main-nav a{color:#fff;text-decoration:none;font-size:12.5px;font-weight:700;letter-spacing:.3px;padding:0 13px;line-height:52px}
.main-nav a.active{background:#3a3a3a}

.hero{position:absolute;top:150px;left:0;width:1200px;height:579px;
  background:
    linear-gradient(180deg,rgba(255,255,255,0) 0%,rgba(255,255,255,0) 70%,rgba(120,110,95,.55) 100%),
    linear-gradient(90deg,#1a5fb8 0%,#2f72c4 30%,#6f9fd6 44%,#d9d2c4 58%,#c8b89c 72%,#a49278 88%,#8a7a66 100%)}
.hero-panel{position:absolute;left:75px;top:82px;width:422px;height:415px;background:rgba(10,14,22,.92);padding:26px 26px;color:#fff}
.hero-panel h1{font-weight:400;font-size:31px;line-height:38px;letter-spacing:.5px}
.perks{list-style:none;margin-top:14px}
.perks li{display:flex;align-items:center;gap:16px;font-size:16px;height:34px}
.btn-outline{display:inline-block;border:2px solid #fff;color:#fff;text-decoration:none;font-size:16px;padding:12px 18px;letter-spacing:.4px}

.apply-form{position:absolute;top:729px;left:0;width:1200px;height:294px;background:var(--dark)}
.field{position:absolute;background:#fff;height:43px;font-size:10px;font-weight:700;color:#333;padding:16px 14px}
.send{position:absolute;left:435px;top:183px;width:332px;height:44px;border:2px solid #fff;color:#fff;font-weight:700;font-size:18px;text-align:center;line-height:40px}

.positions{position:absolute;top:1023px;left:0;width:1200px;height:575px;background:#fff}
.role-card{position:absolute;top:131px;width:242px;height:263px}
.role-label{position:absolute;left:18px;right:18px;bottom:20px;height:43px;background:rgba(255,255,255,.85);text-align:center;line-height:43px;font-weight:700;font-size:16px;color:var(--ink)}
.btn-dark{position:absolute;background:var(--ink);color:#fff;font-size:17px;text-align:center;letter-spacing:.3px}

.how{position:absolute;top:1598px;left:0;width:1200px;height:410px;background:var(--mist)}
.step{position:absolute;top:176px;width:329px;height:172px;background:#fff;border:1px solid var(--line);text-align:center;font-size:18px;line-height:28px;color:var(--ink);padding-top:62px}
.step-icon{position:absolute;left:50%;top:-42px;margin-left:-42px;width:84px;height:84px;border-radius:50%;background:var(--ink);display:flex;align-items:center;justify-content:center}

.certify{position:absolute;top:2008px;left:0;width:1200px;height:334px;background:var(--dark);color:#fff}

.partners{position:absolute;top:2342px;left:0;width:1200px;height:431px;background:#fff}
.badge{position:absolute;width:242px;height:101px;border:1px solid var(--line);display:flex;align-items:center;justify-content:center}
.badge span{display:block;background:var(--badge);border-radius:3px}

.cv{position:absolute;top:2773px;left:0;width:1200px;height:375px;background:var(--mist)}
.cv p{position:absolute;left:75px;top:114px;width:500px;font-size:16.5px;line-height:30.5px;color:#444}

.testimonials{position:absolute;top:3148px;left:0;width:1200px;height:408px;background:#fff}
.quote{position:absolute;left:135px;width:930px;top:124px;text-align:center;font-size:16px;line-height:32px;color:#444}
.dots{position:absolute;top:326px;left:0;width:1200px;display:flex;justify-content:center;gap:9px}
.dots i{width:11px;height:11px;border-radius:50%;background:#555}
.dots i.on{background:#111}

.site-footer{position:absolute;top:3556px;left:0;width:1200px;height:302px;background:#1c1c1c;color:#bbb}
.site-footer h4{font-size:16px;font-weight:700;color:#fff;letter-spacing:.3px}
.site-footer p{font-size:14px;line-height:27px}
.contact-line{display:flex;align-items:center;gap:18px;font-size:14px;margin-top:10px}
.ffield{position:absolute;background:#fff;font-size:11px;font-weight:700;color:#333;padding:14px 14px}
.legal{position:absolute;top:3858px;left:0;width:1200px;height:70px;background:var(--darker);color:#999;font-size:13px}
.social{position:absolute;right:90px;top:28px;display:flex;gap:22px}
.social i{width:14px;height:14px;border-radius:50%;background:#fff;display:block}
</style>
</head>
<body>

<header class="site-header">
  <div class="brand"><span class="brand-mark"></span>NOBLE POSTS ABROAD</div>
  <div class="call">
    <svg width="16" height="16" viewBox="0 0 24 24"><path fill="#1a1a1a" d="M6.6 10.8a15 15 0 0 0 6.6 6.6l2.2-2.2a1 1 0 0 1 1-.25 11.4 11.4 0 0 0 3.6.57 1 1 0 0 1 1 1V20a1 1 0 0 1-1 1A17 17 0 0 1 3 4a1 1 0 0 1 1-1h3.5a1 1 0 0 1 1 1c0 1.25.2 2.45.57 3.57a1 1 0 0 1-.25 1z"/></svg>
    CALL US: 00971 500 318 206
  </div>
</header>
<nav class="main-nav">
  <a class="active">HOME</a><a>FREE APLICATION</a><a>POSITIONS WE HIRE</a><a>HOW TO APPLY</a><a>FREE CERTIFICATION</a><a>PARTNERS</a><a>CV SERVICES</a><a>TESTIMONIALS</a><a>CONTACT US</a>
</nav>

<section class="hero" role="img" aria-label="Baroque royal palace facade under a blue sky">
  <div class="hero-panel">
    <h1>APPLY FOR ROYAL JOBS<br>IN DUBAI</h1>
    <ul class="perks">
      <li><svg width="15" height="15" viewBox="0 0 16 16"><circle cx="8" cy="8" r="8" fill="#fff"/><path d="M4.5 8.3l2.3 2.2 4.7-4.8" stroke="#111" stroke-width="2" fill="none"/></svg>Salary starting 400$ net</li>
      <li><svg width="15" height="15" viewBox="0 0 16 16"><circle cx="8" cy="8" r="8" fill="#fff"/><path d="M4.5 8.3l2.3 2.2 4.7-4.8" stroke="#111" stroke-width="2" fill="none"/></svg>Paid visa</li>
      <li><svg width="15" height="15" viewBox="0 0 16 16"><circle cx="8" cy="8" r="8" fill="#fff"/><path d="M4.5 8.3l2.3 2.2 4.7-4.8" stroke="#111" stroke-width="2" fill="none"/></svg>Given food + accomodation</li>
      <li><svg width="15" height="15" viewBox="0 0 16 16"><circle cx="8" cy="8" r="8" fill="#fff"/><path d="M4.5 8.3l2.3 2.2 4.7-4.8" stroke="#111" stroke-width="2" fill="none"/></svg>Vacation + ticket</li>
      <li><svg width="15" height="15" viewBox="0 0 16 16"><circle cx="8" cy="8" r="8" fill="#fff"/><path d="M4.5 8.3l2.3 2.2 4.7-4.8" stroke="#111" stroke-width="2" fill="none"/></svg>Medical</li>
      <li><svg width="15" height="15" viewBox="0 0 16 16"><circle cx="8" cy="8" r="8" fill="#fff"/><path d="M4.5 8.3l2.3 2.2 4.7-4.8" stroke="#111" stroke-width="2" fill="none"/></svg>Unforms and toiletries</li>
    </ul>
    <a class="btn-outline" style="margin-top:22px">APPLY NOW</a>
  </div>
</section>

<section class="apply-form">
  <h2 class="section-title" style="top:58px;color:#fff">FREE APLICATION FORM</h2>
  <div class="field" style="left:253px;top:120px;width:334px">NAME *</div>
  <div class="field" style="left:613px;top:120px;width:334px">EMAIL ADDRESS *</div>
  <div class="send">SEND</div>
</section>

<section class="positions">
  <h2 class="section-title" style="top:58px;color:var(--ink)">POSITIONS WE HIRE</h2>
  <svg class="abs" style="left:42px;top:247px" width="20" height="32" viewBox="0 0 20 32"><path d="M16 3L4 16l12 13" stroke="#111" stroke-width="4" fill="none"/></svg>
  <svg class="abs" style="left:1140px;top:247px" width="20" height="32" viewBox="0 0 20 32"><path d="M4 3l12 13L4 29" stroke="#111" stroke-width="4" fill="none"/></svg>
  <div class="role-card" style="left:75px;background:linear-gradient(160deg,#efe9e4 0%,#c9b3a5 35%,#9fb1d0 70%,#e9e6ea 100%)" role="img" aria-label="Nanny with a child"><div class="role-label">NANNIES</div></div>
  <div class="role-card" style="left:343px;background:linear-gradient(170deg,#e6ecee 0%,#d8d2cb 45%,#9c9894 70%,#c8c4bf 100%)" role="img" aria-label="Chambermaid in uniform"><div class="role-label">CHAMBERMAID</div></div>
  <div class="role-card" style="left:613px;background:linear-gradient(150deg,#8e8e8c 0%,#c9c6c2 40%,#6a6866 70%,#3e3d3c 100%)" role="img" aria-label="Maternity nurse with a client"><div class="role-label">MATERNITY NURSES</div></div>
  <div class="role-card" style="left:884px;background:linear-gradient(90deg,#d8d8d8 0%,#cfcfcf 25%,#1e1e1e 45%,#262626 60%,#d4d4d4 80%,#dcdcdc 100%)" role="img" aria-label="Butler in tailcoat"><div class="role-label">BUTLERS</div></div>
  <div class="btn-dark" style="left:496px;top:447px;width:208px;height:57px;line-height:57px">VIEW ALL POSITIONS</div>
</section>

<section class="how">
  <h2 class="section-title" style="top:55px;color:var(--ink)">HOW TO APPLY</h2>
  <div class="step" style="left:75px">
    <div class="step-icon"><svg width="40" height="30" viewBox="0 0 40 30"><rect x="3" y="4" width="34" height="22" rx="2" stroke="#fff" stroke-width="2" fill="none"/><rect x="24" y="9" width="9" height="12" stroke="#fff" stroke-width="1.5" fill="none"/><path d="M7 12h13M7 17h10" stroke="#fff" stroke-width="1.5"/></svg></div>
    Free joining visa<br>and ticket
  </div>
  <div class="step" style="left:435px">
    <div class="step-icon"><svg width="34" height="38" viewBox="0 0 34 38"><rect x="4" y="3" width="22" height="30" rx="2" stroke="#fff" stroke-width="2" fill="none"/><path d="M9 20h12M9 25h9" stroke="#fff" stroke-width="1.5"/><circle cx="15" cy="12" r="4" stroke="#fff" stroke-width="1.5" fill="none"/><path d="M30 14l-9 14" stroke="#fff" stroke-width="2"/></svg></div>
    Applicant will never be charged<br>free application &amp; arrival
  </div>
  <div class="step" style="left:795px">
    <div class="step-icon"><svg width="42" height="32" viewBox="0 0 42 32"><path d="M6 6l6 2 8 10 14 4c3 1 3 4 0 4H10L6 6z" stroke="#fff" stroke-width="2" fill="none"/><path d="M4 29h34" stroke="#fff" stroke-width="2"/></svg></div>
    Free safety landing-  own butler<br>will welcome at the airport and<br>free airport transfer
  </div>
</section>

<section class="certify">
  <h2 class="section-title" style="top:88px;color:#fff">FREE CERTIFICATION</h2>
  <p class="abs" style="top:146px;left:0;width:1200px;text-align:center;font-size:18px">Free training programs for the applicants who wish to upgrade their skillset.</p>
  <div class="abs" style="left:435px;top:196px;width:332px;height:44px;border:2px solid #fff;text-align:center;line-height:40px;font-weight:700;font-size:18px">GET YOUT FREE CERTIFICATION</div>
</section>

<section class="partners">
  <h2 class="section-title" style="top:54px;color:var(--ink)">PARTNERS</h2>
  <div class="badge" style="left:75px;top:133px"><span style="width:190px;height:50px"></span></div>
  <div class="badge" style="left:345px;top:133px"><span style="width:170px;height:54px"></span></div>
  <div class="badge" style="left:614px;top:133px"><span style="width:178px;height:56px"></span></div>
  <div class="badge" style="left:884px;top:133px"><span style="width:44px;height:50px"></span></div>
  <div class="badge" style="left:209px;top:257px"><span style="width:178px;height:40px"></span></div>
  <div class="badge" style="left:479px;top:257px"><span style="width:98px;height:40px"></span></div>
  <div class="badge" style="left:749px;top:257px"><span style="width:195px;height:46px"></span></div>
</section>

<section class="cv">
  <h2 class="abs" style="left:73px;top:56px;font-size:33px;font-weight:400;color:var(--ink);letter-spacing:.5px">FREE CV MAKING SERVICE</h2>
  <p>Pellentesque pellentesque diam eget lacus tempus mollis et mollis leo. Etiam blandit mattis lacus vitae maximus. Proin vitae mauris sed erat elementum finibus vel a odio ed blandit a enim sit amet sollicitudin.</p>
  <div class="btn-dark" style="left:75px;top:257px;width:166px;height:57px;line-height:57px">READ MORE</div>
  <div class="abs" style="left:614px;top:0;width:586px;height:375px;background:linear-gradient(120deg,#2f3440 0%,#4c5566 28%,#8a8478 55%,#d9cbb0 78%,#6a5a44 100%)" role="img" aria-label="Person typing a resume on a laptop"></div>
</section>

<section class="testimonials">
  <h2 class="section-title" style="top:60px;color:var(--ink)">TESTIMONIALS</h2>
  <p class="quote">“We travel a lot; my family has three homes based in London-Riga-Vienna. Maison Ardent has found for us a governess and a maid. They travel with us and are happy to be a part of an unusual setting of a family, both by an extrovert one as we hold cocktails so often. Think very soon we will need a chef as well, and there is only one place to search for one!”</p>
  <p class="abs" style="top:242px;left:0;width:1200px;text-align:center;font-weight:700;font-size:16px;color:var(--ink)">Mira T., Latvian – based in London, Riga, Vienna</p>
  <div class="dots"><i class="on"></i><i></i><i></i><i></i></div>
</section>

<footer class="site-footer">
  <div class="abs" style="left:75px;top:58px;width:240px">
    <h4>DUBAI LOCATIONS</h4>
    <p style="margin-top:6px">Meridian Court 14 level,<br>Harbour District Dubai, UAE P.O Box<br>908341 (UAE)</p>
    <div class="contact-line"><svg width="12" height="12" viewBox="0 0 24 24"><path fill="#bbb" d="M6.6 10.8a15 15 0 0 0 6.6 6.6l2.2-2.2a1 1 0 0 1 1-.25 11.4 11.4 0 0 0 3.6.57 1 1 0 0 1 1 1V20a1 1 0 0 1-1 1A17 17 0 0 1 3 4a1 1 0 0 1 1-1h3.5a1 1 0 0 1 1 1c0 1.25.2 2.45.57 3.57a1 1 0 0 1-.25 1z"/></svg>1-800-555-0148</div>
    <div class="contact-line"><svg width="12" height="10" viewBox="0 0 24 18"><path fill="#bbb" d="M0 0h24v18H0z"/><path d="M0 0l12 9 12-9" stroke="#1c1c1c" stroke-width="2" fill="none"/></svg>hello@nobleposts.example</div>
  </div>
  <div class="abs" style="left:343px;top:58px;width:240px">
    <h4>UK LOCATIONS</h4>
    <p style="margin-top:6px">48 Lindale Row,<br>Glasgow G3 7PQ</p>
    <div class="contact-line"><svg width="12" height="12" viewBox="0 0 24 24"><path fill="#bbb" d="M6.6 10.8a15 15 0 0 0 6.6 6.6l2.2-2.2a1 1 0 0 1 1-.25 11.4 11.4 0 0 0 3.6.57 1 1 0 0 1 1 1V20a1 1 0 0 1-1 1A17 17 0 0 1 3 4a1 1 0 0 1 1-1h3.5a1 1 0 0 1 1 1c0 1.25.2 2.45.57 3.57a1 1 0 0 1-.25 1z"/></svg>1-800-555-0148</div>
    <div class="contact-line"><svg width="12" height="10" viewBox="0 0 24 18"><path fill="#bbb" d="M0 0h24v18H0z"/><path d="M0 0l12 9 12-9" stroke="#1c1c1c" stroke-width="2" fill="none"/></svg>hello@nobleposts.example</div>
  </div>
  <h4 class="abs" style="left:617px;top:58px">CONTACT FORM</h4>
  <div class="ffield" style="left:614px;top:95px;width:242px;height:40px">NAME</div>
  <div class="ffield" style="left:614px;top:153px;width:242px;height:40px">EMAIL ADDRESS</div>
  <div class="abs" style="left:614px;top:209px;width:120px;height:37px;border:2px solid #fff;color:#fff;font-size:12px;font-weight:700;text-align:center;line-height:33px">SUBMIT</div>
  <div class="ffield" style="left:884px;top:95px;width:241px;height:98px">MESSAGE</div>
</footer>
<div class="legal">
  <p class="abs" style="left:75px;top:28px">Copyright © 2020 Noble Posts Abroad . All Right Reserved. <b style="color:#fff">Legalities</b></p>
  <div class="social" aria-label="Social links"><i></i><i></i><i></i><i></i><i></i></div>
</div>

</body>
</html>
```